limo company looking for a graphic business card with professional look and feel

Looking for a business card design that can give you the full picture of the limo company by looking at the card - we provide airport service, wedding, birthday, night out, etc... we have sedans, suvs , limos, and party buses. I want the business card to have a professional look because we are targetting corporate clients as well as regular retail.
Info about the business can be found at: http://lnk.example.test/Qm4Tz
Target Market(s)
corporate clients and retail
Industry/Entity Type
Business
Contact Information for Business Card
I would like the logo and the name of the company to be in raised print - not sure if design makes a difference for that or just print - I need it designed in 350dpi
Requirements
Must have
- pictures of vehicle types (sedans, suvs, limos, party bus). pictures of interior of the limos if possible. list service types (weddings, birthdays, proms, airport transportation) & service areas (houston, the woodlands, spring, tomball, cypress, kingwood).
Nice to have
- nice professional look to it.

```html
<!DOCTYPE html>
<html lang="en">
<head>
<meta charset="utf-8">
<title>Crestline Livery &amp; Transportation — Business Card</title>
<link rel="stylesheet" href="https://fonts.googleapis.com/css2?family=Lato:wght@400;700&family=Tinos:wght@700&display=swap">
<style>
  :root {
    --royal: #1d3a94;
    --royal-deep: #162f7d;
    --ink: #1b1b1b;
    --white: #ffffff;
    --paper: #f2f2f2;
    --sky-top: #9fb8d6;
    --sky-low: #c9b79a;
    --water: #5c7a6a;
    --car-top: #3a3d42;
    --car-low: #0e0f11;
    --backdrop: #e4e4e6;
  }
  * { box-sizing: border-box; margin: 0; padding: 0; }
  html, body { width: 1171px; height: 1200px; overflow: hidden; }
  body {
    background: var(--backdrop);
    font-family: "Lato", Arial, sans-serif;
    position: relative;
  }
  .card {
    position: absolute;
    left: 95px;
    width: 980px;
    height: 560px;
    overflow: hidden;
    box-shadow: 0 4px 14px rgba(0,0,0,.18);
  }

  /* ---------- Front ---------- */
  .card-front {
    top: 25px;
    background: var(--royal);
    color: var(--white);
    text-align: center;
  }
  .brand {
    position: absolute;
    top: 70px;
    left: 0; right: 0;
  }
  .brand-name {
    font-weight: 700;
    font-size: 58px;
    letter-spacing: 1px;
    line-height: 1;
  }
  .brand-sub {
    font-weight: 400;
    font-size: 34px;
    margin-top: 8px;
    line-height: 1;
  }
  .fleet {
    position: absolute;
    top: 215px; left: 0; right: 0;
    font-weight: 700;
    font-size: 23px;
  }
  .services {
    position: absolute;
    top: 252px; left: 0; right: 0;
    font-size: 23px;
  }
  .areas-rule {
    position: absolute;
    top: 305px; left: 60px; right: 60px;
    display: flex;
    align-items: center;
    gap: 18px;
    font-size: 22px;
  }
  .areas-rule::before, .areas-rule::after {
    content: "";
    flex: 1;
    height: 2px;
    background: rgba(255,255,255,.8);
  }
  .areas {
    position: absolute;
    top: 345px; left: 0; right: 0;
    font-size: 23px;
  }
  .phones {
    position: absolute;
    top: 410px; left: 0; right: 0;
    display: flex;
    justify-content: center;
    gap: 90px;
    font-family: "Tinos", "Times New Roman", serif;
    font-weight: 700;
  }
  .phone-label { font-size: 24px; }
  .phone-number { font-size: 42px; line-height: 1.15; }

  /* ---------- Back ---------- */
  .card-back {
    top: 615px;
    background: var(--white);
  }
  .back-art {
    position: absolute;
    inset: 0;
    width: 980px;
    height: 560px;
  }
  .tagline {
    position: absolute;
    top: 40px; right: 40px;
    font-family: "Tinos", "Times New Roman", serif;
    font-weight: 700;
    font-size: 32px;
    color: var(--royal);
    letter-spacing: .5px;
  }
  .vehicle-photo {
    position: absolute;
    left: 25px; top: 330px;
    width: 330px; height: 165px;
    border-radius: 60px 90px 22px 22px;
    background: linear-gradient(180deg, var(--car-top), var(--car-low));
  }
  .back-brand {
    position: absolute;
    right: 45px; top: 420px;
    text-align: center;
    color: var(--ink);
  }
  .back-brand .brand-name { font-size: 36px; }
  .back-brand .brand-sub { font-size: 22px; margin-top: 6px; }
  .base-band {
    position: absolute;
    left: 0; right: 0; bottom: 0;
    height: 22px;
    background: var(--royal);
  }
</style>
</head>
<body>

<section class="card card-front" aria-label="Business card front">
  <div class="brand">
    <div class="brand-name">Crestline Livery</div>
    <div class="brand-sub">&amp; Transportation</div>
  </div>
  <p class="fleet">Sedans, Suvs, Limos, Party Bus</p>
  <p class="services">• Weddings • Birthdays • Proms • Airport Transportation</p>
  <p class="areas-rule">Service Areas</p>
  <p class="areas">• Houston • The Woodlands • Spring • Tomball • Cypress • Kingwood</p>
  <div class="phones">
    <div class="phone">
      <div class="phone-label">Call Toll Free:</div>
      <div class="phone-number">(800)555-0143</div>
    </div>
    <div class="phone">
      <div class="phone-label">Call Us Direct:</div>
      <div class="phone-number">(832)555-0198</div>
    </div>
  </div>
</section>

<section class="card card-back" aria-label="Business card back">
  <svg class="back-art" viewBox="0 0 980 560" aria-hidden="false">
    <defs>
      <linearGradient id="skyline" x1="0" y1="0" x2="0" y2="1">
        <stop offset="0" stop-color="var(--sky-top)"/>
        <stop offset="0.55" stop-color="var(--sky-low)"/>
        <stop offset="1" stop-color="var(--water)"/>
      </linearGradient>
    </defs>
    <path role="img" aria-label="Photo of a city skyline with a river and arched bridge"
          d="M0 0 H980 V330 C820 300 640 300 470 325 C300 350 150 330 0 300 Z"
          fill="url(#skyline)"/>
    <path d="M0 300 C150 330 300 350 470 325 C640 300 820 300 980 330"
          fill="none" stroke="var(--royal)" stroke-width="10"/>
  </svg>
  <p class="tagline">LIMO SERVICE</p>
  <div class="vehicle-photo" role="img" aria-label="Photo of a black luxury sedan"></div>
  <div class="back-brand">
    <div class="brand-name">Crestline Livery</div>
    <div class="brand-sub">&amp; Transportation</div>
  </div>
  <div class="base-band"></div>
</section>

</body>
</html>
```